■依頼の目的/概要
ハルカゼのlumoraで電子書籍出版をします。

■本の内容
40代女性で話すことや伝えること
自分に自信はないけれど

起業したい、
夢や目標を叶えたい、
という方がターゲットです。

声と潜在意識(心)の力を使う「ひだまりトーン」で
人前で自信をもって伝えられるようになったり
やりたいことがどんどん実現できるようになる方法を
書きました。

声や潜在意識を使ったトレーニング、
実例を用いてお伝えしています。

■デザイン要望
40代女性が好むデザインが希望です。
顔写真も入れていただけたらと思います。
その際、手に持っている音符などは載せないようお願いいたします。

お写真と、電子書籍の文章をお送りいたします。

ご応募、心よりお待ちしております!!!

その他何かご不明な点がございましたら、お気軽にご質問下さい。
よろしくお願いいたします。
タイトルは
響きの名手がひもとく
輝く毎日をつくる心の整え方・磨き方
~ひだまりトーンの秘密~

著者は
ひだまりトーンコンサルタント
さとうれな

どうぞよろしくお願いいたします。
LQS表記では、表紙画像のサイズは 50 MB 未満表紙フ
ァイルの理想的な寸法は 2,560 x 1,600 ピクセルとなっています。

文字が見やすいこと。
女性的な優しいイメージと内容が合うもの、
という視点で選ばせていただきました。

素晴らしい作品ばかりで
選ばせていただくのに時間がかかりました。

短期間にも関わらず
素敵な作品を沢山ご応募いただき
どうもありがとうございました!

心より感謝いたします。

機会がございましたら
またどうぞよろしくお願いいたします。

```html
<!DOCTYPE html>
<html lang="ja">
<head>
<meta charset="utf-8">
<title>輝く毎日をつくる心の整え方・磨き方</title>
<link href="https://fonts.googleapis.com/css2?family=Noto+Serif+JP:wght@500;700;900&family=Noto+Sans+JP:wght@500;700;900&family=Great+Vibes&family=Klee+One:wght@600&display=swap" rel="stylesheet">
<style>
:root{
  --mint-top:#d6efe1;
  --mint-mid:#e6f5ec;
  --green-band:#86cfa9;
  --green-deep:#6bbf95;
  --pink:#e2607f;
  --pink-soft:#f2b3c2;
  --ink:#3a3a3a;
  --paper:#ffffff;
  --frame:#e9d3bd;
  --cream:#fbf6f4;
}
*{margin:0;padding:0;box-sizing:border-box}
html,body{width:750px;height:1200px;overflow:hidden}
body{position:relative;background:var(--cream);font-family:"Noto Sans JP",sans-serif;color:var(--ink)}
.cover-top{position:absolute;left:0;top:0;width:750px;height:830px;
  background:linear-gradient(180deg,var(--mint-top) 0,var(--mint-mid) 440px,var(--green-band) 441px,var(--green-deep) 830px)}
.kicker{position:absolute;top:48px;left:0;width:750px;text-align:center;
  font-family:"Noto Serif JP",serif;font-weight:700;font-size:40px;letter-spacing:6px;color:var(--ink)}
.title-card{position:absolute;left:50px;top:122px;width:650px;height:690px;background:var(--paper);
  box-shadow:0 4px 14px rgba(0,0,0,.12)}
.title-card::before{content:"";position:absolute;inset:14px;border:2px solid var(--frame)}
.illustration{position:absolute;left:42px;top:28px;width:140px;height:170px;border-radius:70px 70px 20px 20px;
  background:linear-gradient(180deg,#f3e1d4,#e9cdb8)}
.lead{position:absolute;top:58px;left:200px;right:20px;text-align:center;
  font-family:"Noto Serif JP",serif;font-weight:900;font-size:48px;color:var(--pink);letter-spacing:2px;white-space:nowrap}
.subhead{position:absolute;top:124px;left:210px;right:20px;text-align:center;
  font-family:"Noto Serif JP",serif;font-weight:900;font-size:56px;color:var(--ink);letter-spacing:2px}
.main-title{position:absolute;left:0;width:650px;text-align:center;
  font-family:"Noto Sans JP",sans-serif;font-weight:900;font-size:150px;line-height:1;color:var(--ink);letter-spacing:6px}
.main-title.one{top:202px}
.main-title.two{top:362px}
.series-band{position:absolute;left:85px;top:528px;width:480px;height:58px;background:var(--pink);
  color:#fff;text-align:center;line-height:58px;font-family:"Noto Serif JP",serif;font-weight:700;font-size:32px;letter-spacing:1px;white-space:nowrap}
.tagline{position:absolute;left:20px;top:606px;width:610px;text-align:center;white-space:nowrap;
  font-family:"Great Vibes",cursive;font-size:30px;color:var(--pink-soft)}
.promise{position:absolute;left:48px;top:858px;font-family:"Noto Sans JP",sans-serif;font-weight:900;color:var(--ink)}
.promise .small{display:block;font-size:44px;line-height:56px;letter-spacing:1px}
.promise .large{display:block;font-size:62px;line-height:80px;letter-spacing:2px;margin-top:4px}
.divider{position:absolute;left:48px;top:1004px;width:300px;height:3px;background:var(--pink)}
.author-label{position:absolute;left:48px;top:1014px;font-weight:900;font-size:30px;line-height:40px;color:var(--pink)}
.author-role{position:absolute;left:48px;top:1054px;font-weight:700;font-size:24px;line-height:32px;color:var(--pink)}
.author-name{position:absolute;left:48px;top:1096px;font-family:"Noto Serif JP",serif;font-weight:900;font-size:64px;line-height:80px;color:var(--pink);letter-spacing:6px}
.author-note{position:absolute;left:396px;top:1030px;transform:rotate(-14deg);
  font-family:"Klee One",cursive;font-weight:600;font-size:19px;line-height:1.3;color:var(--pink);text-align:center}
.author-portrait{position:absolute;left:470px;top:842px;width:300px;height:300px;border-radius:50%;
  background:radial-gradient(circle at 50% 45%,#f4dccf 0,#d9b7a4 55%,#5b4038 100%)}
</style>
</head>
<body>
  <div class="cover-top"></div>
  <p class="kicker">響きの名手がひもとく</p>

  <section class="title-card">
    <div class="illustration" role="img" aria-label="ポインターを持つ女性のイラスト"></div>
    <p class="lead">輝く毎日をつくる</p>
    <p class="subhead">心の</p>
    <h1 class="main-title one">整え方</h1>
    <h1 class="main-title two">磨き方</h1>
    <p class="series-band">〜ひだまりトーンの秘密〜</p>
    <p class="tagline">Make a wish come true &nbsp;How to speak &nbsp;How to tell</p>
  </section>

  <div class="author-portrait" role="img" aria-label="著者の顔写真"></div>

  <p class="promise"><span class="small">ひだまりトーンで</span><span class="large">人生が変わる</span></p>
  <div class="divider"></div>
  <p class="author-label">著者</p>
  <p class="author-role">ひだまりトーンコンサルタント</p>
  <p class="author-name">さとう れな</p>
  <p class="author-note">ワタシに<br>お任せください!</p>
</body>
</html>
```